World leading Water filters German made

I am a local Plumbing business who is authorised water filter installer
I want to do a Flyer design double sided targeting niche market for Water Filters.
My company colours are black background with white writing.
( but happy to go into different colours to capture more people )
I want all my stuff, sleek and professional with the same fonts throughout.
Www.brightvalepipeworks.au
Is my website you can see how I do things there.
I want the local business awards finalist logo on the flyer too ( it’ll be in the photo)
This Flyer I want all about health and wellness making big points on water filtration benefits
Massive to included HYDROGEN WATER AND ALKALINE WATER ,
REMOVE FLUORIDE
I don’t know whether to have it with the pre-save branded information I sent over, but I don’t want the company other companies name everywhere
I want the main focus about my company Brightvale Pipeworks And Boiler Experts
I want the focus to be about a family owned and run Illawarra local business establish for over 20 years.
Please note I have included a Customer brochure the company has designed so you can see some key points on the second page about the products. I want this a lot more eye-catching and appealing please
Target Market(s)
Health and wellness people
Colors
Designer to choose colors to be used in the design.
Requirements
Must have
- Call Trevor 0487 263 915, my website , social media buttons ,
Nice to have
- World leading , health and wellness ,
Should not have
- Any information to lead them away from calling myself , I’m the authorities dealer for aqua crest supply but I want to no have as much anout them.

```html
<!DOCTYPE html>
<html lang="en">
<head>
<meta charset="utf-8">
<title>Brightvale Pipeworks – Water Filters Flyer</title>
<link href="https://fonts.googleapis.com/css2?family=Exo+2:wght@600;700;800;900&family=Roboto:wght@400;500;700&display=swap" rel="stylesheet">
<style>
:root{
  --stage:#d3d8dd;
  --blue:#2f5fc8;
  --blue-bright:#3a6ee0;
  --navy:#17265a;
  --ink:#0c1222;
  --pale:#8ea6dc;
  --white:#ffffff;
  --text:#1b1b1b;
  --gold:#c9a24a;
  --star:#f6c21a;
}
*{box-sizing:border-box;margin:0;padding:0}
html,body{width:1200px;height:1200px;overflow:hidden;background:var(--stage)}
body{position:relative;font-family:'Roboto',Arial,sans-serif;color:var(--text)}
.page{position:absolute;top:254px;width:534px;height:691px;background:var(--white);overflow:hidden}
.page--front{left:48px}
.page--back{left:616px}
.abs{position:absolute}
.heading{font-family:'Exo 2',Arial,sans-serif}

/* front */
.hero-photo{left:0;top:0;width:534px;height:204px;background:linear-gradient(100deg,#1a2230 0%,#3a4a62 35%,#5f7697 60%,var(--blue) 100%)}
.hero-title{left:280px;top:34px;width:236px;text-align:center;color:var(--white)}
.hero-title__kicker{font-family:'Exo 2',sans-serif;font-weight:800;font-size:19px;letter-spacing:.5px}
.hero-title__main{font-family:'Exo 2',sans-serif;font-weight:900;font-size:52px;line-height:42px;letter-spacing:1px;margin-top:2px}
.hero-title__badge{display:block;margin:6px auto 0;width:228px;background:var(--ink);border:2px solid var(--white);font-family:'Exo 2',sans-serif;font-weight:800;font-size:20px;line-height:24px;letter-spacing:1px}
.feature-line{left:0;width:534px;text-align:center;font-family:'Exo 2',sans-serif;font-weight:800;color:var(--ink)}
.feature-line--top{top:205px;font-size:20px}
.feature-line--sub{top:228px;font-size:17px;display:flex;align-items:center;justify-content:center;gap:12px}
.feature-line--sub::before,.feature-line--sub::after{content:"";width:140px;height:3px;background:var(--blue)}
.side-panel{left:14px;top:256px;width:226px;height:435px;background:linear-gradient(180deg,var(--blue) 0%,var(--navy) 55%,var(--ink) 100%)}
.award-badge{left:26px;top:270px;width:56px;height:85px;background:linear-gradient(180deg,#e0c27a,var(--gold) 60%,#8a0f1a 60%)}
.call-box{left:84px;top:282px;width:144px;height:58px;background:var(--white);text-align:center;padding-top:6px}
.call-box__big{font-family:'Exo 2',sans-serif;font-weight:900;font-size:25px;line-height:24px;color:var(--blue)}
.call-box__small{font-family:'Exo 2',sans-serif;font-weight:700;font-size:19px;line-height:22px;color:var(--ink)}
.checklist{left:44px;top:376px;list-style:none}
.checklist li{display:flex;align-items:center;gap:10px;height:35px;color:var(--white);font-family:'Exo 2',sans-serif;font-weight:700;font-size:12px;line-height:12px;letter-spacing:.4px}
.checklist svg{flex:none}
.brand-name{text-align:center;color:var(--white);font-family:'Exo 2',sans-serif;font-weight:900;letter-spacing:.5px}
.brand-name--front{left:34px;top:564px;width:190px;font-size:19px;line-height:20px}
.intro{left:256px;top:266px;width:252px;font-size:9.6px;line-height:12.2px;text-align:justify;color:#222}
.section-bar{height:24px;background:var(--blue);color:var(--white);font-family:'Exo 2',sans-serif;font-weight:800;font-size:16px;line-height:24px;text-align:center;letter-spacing:.5px;border-right:5px solid var(--navy)}
.services-bar{left:256px;top:367px;width:260px}
.services{left:256px;top:400px;width:254px;text-align:center;font-family:'Roboto',sans-serif;font-weight:700;font-size:11px;line-height:14px;color:var(--ink)}
.services b{color:var(--blue)}
.product-shot{left:258px;top:508px;width:248px;height:138px;background:linear-gradient(90deg,#b8bcc2,#eef0f3 45%,#3f6fd0 75%,#1a1f2a)}
.product-tag{left:370px;top:622px;width:136px;text-align:center;background:rgba(255,255,255,.9)}
.product-tag__title{font-family:'Exo 2',sans-serif;font-weight:700;font-size:11px;color:var(--navy)}
.product-tag__sub{font-size:7px;color:var(--blue)}
.contact-bar{left:36px;top:651px;width:470px;height:27px;background:var(--blue);color:var(--white);font-family:'Exo 2',sans-serif;font-weight:700;font-size:16px;line-height:27px;text-align:center;letter-spacing:.5px}

/* back */
.back-bar{left:8px;width:258px;font-size:15px}
.bar-world{top:10px}
.bar-remove{top:142px}
.bar-health{top:216px}
.bullets{left:10px;width:256px;list-style:none;font-size:9.5px;line-height:12px;color:#222}
.bullets li::before{content:"•";color:var(--blue);font-weight:700;margin-right:4px}
.bullets--world{top:45px}
.bullets--health{top:247px}
.remove-list{left:8px;top:172px;width:258px;text-align:center;font-size:9.5px;line-height:12px;color:#222}
.remove-list b{color:var(--blue)}
.wellness-photo{left:0;top:364px;width:290px;height:184px;background:linear-gradient(90deg,#eef1f5,#dfe3e8 50%,#f5f6f8)}
.gallery{left:290px;top:0;width:244px;height:548px;background:var(--pale)}
.gallery-shot{background:linear-gradient(135deg,#e9ecf0,#c4cad2)}
.shot-product{left:299px;top:12px;width:222px;height:130px;background:linear-gradient(90deg,#f4f5f7,#e2e6ec)}
.promo-box{left:299px;top:142px;width:222px;height:96px;background:var(--navy);color:var(--white);padding:10px 10px 0 14px}
.promo-box__title{font-size:15px;line-height:16px;font-weight:400}
.promo-box__fine{font-size:5px;line-height:6px;margin-top:5px;color:#c9d4f0;width:190px}
.promo-strip{left:299px;top:221px;width:222px;height:17px;background:var(--white);text-align:right;padding-right:8px;font-family:'Exo 2',sans-serif;font-size:8px;font-weight:700;line-height:17px;color:var(--navy)}
.shot-unit-a{left:299px;top:242px;width:107px;height:148px;background:linear-gradient(160deg,#6d7b8b,#b9c0c8 50%,#5a6774)}
.shot-unit-b{left:410px;top:242px;width:111px;height:148px;background:linear-gradient(160deg,#8a4b36,#c5c9ce 50%,#7a4030)}
.shot-sink{left:299px;top:394px;width:222px;height:141px;background:linear-gradient(180deg,#e7e9ec,#bfc4ca)}
.back-footer{left:0;top:548px;width:534px;height:143px;background:linear-gradient(180deg,var(--navy),var(--ink))}
.brand-name--back{left:34px;top:562px;width:190px;font-size:19px;line-height:20px}
.stars{left:307px;top:553px;display:flex;gap:4px}
.reviews{left:242px;top:582px;width:246px;text-align:center;color:var(--white);font-size:8.4px;line-height:10.5px}
.reviews p+p{margin-top:8px}
.url-bar{left:38px;top:654px;width:468px;height:25px;background:var(--white);color:var(--navy);font-family:'Exo 2',sans-serif;font-weight:700;font-size:16px;line-height:25px;text-align:center;letter-spacing:.5px}
</style>
</head>
<body>

<section class="page page--front" aria-label="Flyer front">
  <div class="abs hero-photo" role="img" aria-label="Photo of a modern black kitchen tap filling a glass of water"></div>
  <div class="abs hero-title">
    <div class="hero-title__kicker">★ WORLD LEADING ★</div>
    <div class="hero-title__main">WATER<br>FILTERS</div>
    <span class="hero-title__badge">GERMAN MADE</span>
  </div>

  <h1 class="abs feature-line feature-line--top">HYDROGEN WATER &amp; ALKALINE WATER</h1>
  <h2 class="abs feature-line feature-line--sub">REMOVE FLUORIDE</h2>

  <div class="abs side-panel"></div>
  <div class="abs award-badge" role="img" aria-label="Local business awards finalist badge"></div>
  <div class="abs call-box">
    <div class="call-box__big">CALL US</div>
    <div class="call-box__small">TO INSTALL</div>
  </div>

  <ul class="abs checklist">
    <li><svg width="26" height="26" viewBox="0 0 26 26"><rect x="2" y="5" width="19" height="19" fill="none" stroke="#fff" stroke-width="2.5"/><path d="M6 14l5 5L24 3" fill="none" stroke="#fff" stroke-width="3.5"/></svg>AVAILABLE 24/7</li>
    <li><svg width="26" height="26" viewBox="0 0 26 26"><rect x="2" y="5" width="19" height="19" fill="none" stroke="#fff" stroke-width="2.5"/><path d="M6 14l5 5L24 3" fill="none" stroke="#fff" stroke-width="3.5"/></svg>FULLY LICENSED<br>&amp; INSURED</li>
    <li><svg width="26" height="26" viewBox="0 0 26 26"><rect x="2" y="5" width="19" height="19" fill="none" stroke="#fff" stroke-width="2.5"/><path d="M6 14l5 5L24 3" fill="none" stroke="#fff" stroke-width="3.5"/></svg>FAMILY RUN<br>LOCAL BUSINESS</li>
    <li><svg width="26" height="26" viewBox="0 0 26 26"><rect x="2" y="5" width="19" height="19" fill="none" stroke="#fff" stroke-width="2.5"/><path d="M6 14l5 5L24 3" fill="none" stroke="#fff" stroke-width="3.5"/></svg>LIFETIME LABOUR<br>WARRANTY</li>
    <li><svg width="26" height="26" viewBox="0 0 26 26"><rect x="2" y="5" width="19" height="19" fill="none" stroke="#fff" stroke-width="2.5"/><path d="M6 14l5 5L24 3" fill="none" stroke="#fff" stroke-width="3.5"/></svg>FIXED UPFRONT<br>PRICING</li>
  </ul>

  <div class="abs brand-name brand-name--front">BRIGHTVALE<br>PIPEWORKS<br>&amp; BOILER<br>EXPERTS</div>

  <p class="abs intro">A family owned and run Illawarra local business establish for over 20 years, experienced in the plumbing industry, our company offers a friendly and honest service whilst bringing affordability back into the plumbing industry. We provide same day plumbing service throughout the Illawarra, Wollongong, Shellharbour &amp; Shoalhaven areas.</p>

  <div class="abs section-bar services-bar">OUR SERVICES</div>
  <p class="abs services">PLUMBING MAINTENANCE <b>•</b> HOT WATER SYSTEMS <b>•</b> HOT WATER SERVICING <b>•</b> BLOCK DRAINS <b>•</b> LEAK DETECTION <b>•</b> WATER FILTERS <b>•</b> GAS PLUMBER <b>•</b> EMERGENCY PLUMBERS <b>•</b> TOILET REPAIRS &amp; TAP SERVICING</p>

  <div class="abs product-shot" role="img" aria-label="Stainless steel filter unit, Torrent Pro box and three filter cartridges"></div>
  <div class="abs product-tag">
    <div class="product-tag__title">Authorised Distributor</div>
    <div class="product-tag__sub">aqua crest supply</div>
  </div>

  <div class="abs contact-bar">0487 263 915 &nbsp;|&nbsp; brightvalepipeworks.au</div>
</section>

<section class="page page--back" aria-label="Flyer back">
  <div class="abs section-bar back-bar bar-world">WORLD LEADING</div>
  <ul class="abs bullets bullets--world">
    <li>Australian, German &amp; Japanese Designed</li>
    <li>100% Renewable</li>
    <li>100% Sustainable</li>
    <li>1000% Greater Absorption</li>
    <li>Robust Design</li>
    <li>Robust Warranty</li>
    <li>Adopted throughout Europe and the USA</li>
  </ul>

  <div class="abs section-bar back-bar bar-remove">REMOVE &amp; IMPROVE</div>
  <p class="abs remove-list">Chlorine 99.99% <b>•</b> Chloramine 99.99% <b>•</b> Fluoride <b>•</b><br>Heavy Metals <b>•</b> Bacteria <b>•</b> Parasites <b>•</b> Pesticides <b>•</b><br>Hard Water <b>•</b> PFA'S</p>

  <div class="abs section-bar back-bar bar-health">HEALTH BENEFITS</div>
  <ul class="abs bullets bullets--health">
    <li>Reduce the risk of cancer</li>
    <li>Relief for eczema sufferers</li>
    <li>Anti-Aging benefits</li>
    <li>Reduce the risk of birth defects</li>
    <li>Relief for asthma sufferers</li>
    <li>Enjoy chemical free showering</li>
    <li>Healthier drinking water</li>
    <li>Alkaline water</li>
    <li>Hydrogen rich water</li>
  </ul>

  <div class="abs wellness-photo" role="img" aria-label="Photo of a woman drinking a glass of filtered water"></div>

  <div class="abs gallery"></div>
  <div class="abs shot-product" role="img" aria-label="Reverse osmosis filter system with tank and product box"></div>
  <div class="abs promo-box">
    <div class="promo-box__title">Clearstream-RO<br>the future in<br>water filtration.</div>
    <p class="promo-box__fine">A sustainable filtration system that removes harmful chemicals, including chlorine and fluoride, from every tap in your home.</p>
  </div>
  <div class="abs promo-strip">Authorised Distributor</div>
  <div class="abs shot-unit-a" role="img" aria-label="Installed stainless steel whole-house filter unit"></div>
  <div class="abs shot-unit-b" role="img" aria-label="Stainless steel filter unit mounted on a brick wall"></div>
  <div class="abs shot-sink" role="img" aria-label="Under-sink filter installation inside a kitchen cabinet"></div>

  <div class="abs back-footer"></div>
  <div class="abs brand-name brand-name--back">BRIGHTVALE<br>PIPEWORKS<br>&amp; BOILER<br>EXPERTS</div>
  <div class="abs stars" aria-label="Five star rating">
    <svg width="20" height="20" viewBox="0 0 20 20"><polygon points="10,1 12.6,7 19,7.4 14,11.6 15.6,18.6 10,14.8 4.4,18.6 6,11.6 1,7.4 7.4,7" fill="#f6c21a"/></svg>
    <svg width="20" height="20" viewBox="0 0 20 20"><polygon points="10,1 12.6,7 19,7.4 14,11.6 15.6,18.6 10,14.8 4.4,18.6 6,11.6 1,7.4 7.4,7" fill="#f6c21a"/></svg>
    <svg width="20" height="20" viewBox="0 0 20 20"><polygon points="10,1 12.6,7 19,7.4 14,11.6 15.6,18.6 10,14.8 4.4,18.6 6,11.6 1,7.4 7.4,7" fill="#f6c21a"/></svg>
    <svg width="20" height="20" viewBox="0 0 20 20"><polygon points="10,1 12.6,7 19,7.4 14,11.6 15.6,18.6 10,14.8 4.4,18.6 6,11.6 1,7.4 7.4,7" fill="#f6c21a"/></svg>
    <svg width="20" height="20" viewBox="0 0 20 20"><polygon points="10,1 12.6,7 19,7.4 14,11.6 15.6,18.6 10,14.8 4.4,18.6 6,11.6 1,7.4 7.4,7" fill="#f6c21a"/></svg>
  </div>
  <div class="abs reviews">
    <p>Great company fair price, good communication, helpful and made the experience not stressful - MARGOT ELLISON</p>
    <p>Awesome guys, arrived on time and had expertise that will save us so much on costs. Highly recommended.<br>- DELPHINE CARVER</p>
  </div>
  <div class="abs url-bar">0487 263 915 &nbsp;|&nbsp; brightvalepipeworks.au</div>
</section>

</body>
</html>
```